PowerPoint Template Needed for Investment Firm

Norvelle Capital Management is an emerging wealth management firm based in New Jersey. It offers superior investment returns to high net worth individuals and institutions by finding undervalued assets.

We recently selected a company logo which was inspired by the Tucana constellation. Beta Tucanae is a group of six stars, containing star cluster 47 Tucanae, rated the second brightest object in the sky.

Now we need a PowerPoint template with the designs for the following:

1. Title/cover page slide
2. Content slide with title
3. Section slide - to introduce a new section
4. Final slide - with contact information

The slides will be used at investor presentations, that is, to provide information about the company to potential investors. Since we are an investment firm, the design should project a sense of stability, growth and professionalism. The owner is interested in something simple yet striking, which of course is consistent with the logo. I'm thinking more conservative colors and Sans Serif fonts.

I plan on changing the status to non-refundable once I see some designs that I really like.

Target Market(s)

Wealthy individuals, probably middle aged or older, in the US

Industry/Entity Type

Conservative

Requirements
Must have
• Sans serif fonts
Clean, very professional look
Conservative colors that complement existing logo
Should not have
• Anything too busy or complicated

```html
<!DOCTYPE html>
<html lang="en">
<head>
<meta charset="utf-8">
<title>Norvelle Capital Management – Title Slide</title>
<link href="https://fonts.googleapis.com/css2?family=PT+Sans:wght@400;700&display=swap" rel="stylesheet">
<style>
  :root {
    --navy: #1a3aa8;
    --photo-deep: #1d3285;
    --photo-mid: #3f5bb8;
    --photo-light: #8d9fd6;
    --shadow-band: #6b6b6b;
    --subtitle-grey: #8a8a8a;
    --brand-grey: #3d3d3d;
    --brand-square: #1f33a6;
    --paper: #ffffff;
  }
  * { box-sizing: border-box; margin: 0; padding: 0; }
  html, body { width: 1200px; height: 900px; overflow: hidden; background: var(--paper); }
  .slide {
    position: relative;
    width: 1200px;
    height: 900px;
    background: var(--paper);
    font-family: "PT Sans", sans-serif;
  }
  .hero-shadow {
    position: absolute;
    left: 0; top: 20px;
    width: 1200px; height: 712px;
    background: var(--shadow-band);
    border-radius: 0 0 14px 14px;
  }
  .hero-photo {
    position: absolute;
    left: 0; top: 0;
    width: 1200px; height: 702px;
    border-radius: 0 0 14px 14px;
    background:
      radial-gradient(ellipse 60% 55% at 78% 22%, var(--photo-light) 0%, rgba(141,159,214,0) 70%),
      radial-gradient(ellipse 45% 40% at 10% 10%, #6d84cc 0%, rgba(109,132,204,0) 70%),
      linear-gradient(165deg, var(--photo-mid) 0%, #3550a8 45%, var(--photo-deep) 100%);
  }
  .title-bar {
    position: absolute;
    left: 0; top: 482px;
    width: 935px; height: 85px;
    background: var(--paper);
    box-shadow: 2px 3px 6px rgba(0,0,0,0.25);
    display: flex;
    align-items: center;
    padding-left: 37px;
  }
  .title {
    font-size: 50px;
    font-weight: 400;
    color: var(--navy);
    letter-spacing: 0.5px;
  }
  .subtitle {
    position: absolute;
    left: 37px; top: 750px;
    font-size: 37px;
    font-weight: 400;
    color: var(--subtitle-grey);
    letter-spacing: 0.3px;
  }
  .brand {
    position: absolute;
    right: 14px; top: 763px;
    width: 190px;
    display: flex;
    flex-direction: column;
    align-items: center;
  }
  .brand-square {
    width: 77px; height: 76px;
    border-radius: 8px;
    background: var(--brand-square);
  }
  .brand-name {
    margin-top: 8px;
    font-size: 15px;
    font-weight: 400;
    color: var(--brand-grey);
    text-align: center;
    line-height: 1.2;
  }
</style>
</head>
<body>
  <main class="slide">
    <div class="hero-shadow"></div>
    <div class="hero-photo" role="img" aria-label="Blue-toned photo of a calculator and a pen resting on a newspaper page about the global economy"></div>
    <div class="title-bar">
      <h1 class="title">PRESENTATION TITLE</h1>
    </div>
    <p class="subtitle">Presentation subtitle and / or speaker</p>
    <div class="brand">
      <div class="brand-square"></div>
      <p class="brand-name">Norvelle<br>Capital Management</p>
    </div>
  </main>
</body>
</html>
```